RVM Photography Business Card Design

I would like a business card designed in the shape of a camera.
Would like to see various camera designs. Would like to see what the card looks like in different colors. Would like to see which logo looks better on the various camera designs so please show me some with the white logo and some with the black logo. If you need a different file formats please let me know.
Project Deadline Extended Reason: My grandfather passed away and dealing with funeral plans so need to extend deadline. Added Tuesday, March 1, 2016
Project Deadline Extended
Reason: I just got back from out of town. My grandfather's passing was the primary focus for me these past few weeks and the funeral is over so now I will concentrate on picking my business card design. I really appreciate each designer who has taken the time to submit a design. Your effort has not gone unnoticed. I look forward to seeing more amazing designs.
Industry/Entity Type
Business
Contact Information for Business Card
Corinne
757-418-2296
https://www.facebook.com/rvmphotographyfreelance/
NoraCorinne@rvm-studiowork.example

```html
<!DOCTYPE html>
<html lang="en">
<head>
<meta charset="utf-8">
<title>RVM Photography – Camera Business Card</title>
<link rel="stylesheet" href="https://fonts.googleapis.com/css2?family=Montserrat:wght@400;500&display=swap">
<style>
  :root {
    --gold-light: #f7e27a;
    --gold: #eccb1f;
    --gold-deep: #d8b40f;
    --rim-dark: #8d861c;
    --rim-light: #f4f0d2;
    --ink: #000000;
    --text-dark: #2b2a2a;
    --name-gold: #f0cf2a;
    --brand-gold: #d4a94a;
    --page: #ffffff;
  }
  html, body {
    margin: 0;
    padding: 0;
    width: 1200px;
    height: 802px;
    overflow: hidden;
    background: var(--page);
  }
  .card {
    position: relative;
    width: 1200px;
    height: 802px;
    font-family: "Montserrat", Arial, sans-serif;
  }
  .camera-shape {
    position: absolute;
    inset: 0;
    display: block;
  }
  .holder-name {
    position: absolute;
    left: 129px;
    top: 232px;
    margin: 0;
    font-size: 40px;
    font-weight: 500;
    letter-spacing: 0.5px;
    color: var(--name-gold);
  }
  .phone-label {
    position: absolute;
    left: 131px;
    top: 482px;
    margin: 0;
    font-size: 32px;
    font-weight: 400;
    color: var(--text-dark);
  }
  .phone-number {
    position: absolute;
    left: 129px;
    top: 542px;
    margin: 0;
    font-size: 39px;
    font-weight: 400;
    white-space: nowrap;
    color: var(--text-dark);
  }
  .brand {
    position: absolute;
    left: 768px;
    top: 340px;
    transform: translateX(-50%);
    display: flex;
    flex-direction: column;
    align-items: center;
  }
  .brand-dot {
    width: 128px;
    height: 128px;
    border-radius: 50%;
    background: var(--brand-gold);
  }
  .brand-name {
    margin: 26px 0 0;
    font-size: 36px;
    font-weight: 400;
    letter-spacing: 1px;
    white-space: nowrap;
    color: var(--brand-gold);
  }
</style>
</head>
<body>
<main class="card">
  <svg class="camera-shape" width="1200" height="802" viewBox="0 0 1132 757" aria-hidden="true">
    <defs>
      <linearGradient id="body-fill" x1="0" y1="0" x2="0" y2="1">
        <stop offset="0" stop-color="var(--gold-light)"/>
        <stop offset="0.55" stop-color="var(--gold)"/>
        <stop offset="1" stop-color="var(--gold-deep)"/>
      </linearGradient>
    </defs>

    <path class="body-outline"
      d="M30 250 Q30 128 152 128 L190 128 L198 98 Q202 86 216 86 L284 86 Q296 86 300 98 L306 128 L335 128 L335 62 Q335 28 370 28 L730 28 Q765 28 765 62 L765 128 L975 128 Q1097 128 1097 250 L1097 520 Q1097 642 975 642 L152 642 Q30 642 30 520 Z"
      fill="url(#body-fill)" stroke="var(--rim-dark)" stroke-width="7"/>
    <path class="body-highlight"
      d="M40 250 Q40 138 152 138 L196 138 L206 100 Q209 96 216 96 L284 96 Q290 96 292 102 L298 138 L345 138 L345 62 Q345 38 370 38 L730 38 Q755 38 755 62 L755 138 L975 138 Q1087 138 1087 250 L1087 520 Q1087 632 975 632 L152 632 Q40 632 40 520 Z"
      fill="none" stroke="var(--rim-light)" stroke-width="2" opacity="0.8"/>

    <path class="top-band"
      d="M75 232 Q78 165 150 165 L385 165 L385 88 Q385 68 406 68 L692 68 Q712 68 712 88 L712 165 L958 165 Q1052 165 1052 262 L1052 332 Q1010 300 950 292 L440 292 Q380 292 340 300 L75 330 Z"
      fill="var(--ink)" stroke="var(--rim-light)" stroke-width="4"/>

    <rect class="shutter" x="460" y="108" width="176" height="52" rx="26"
      fill="var(--gold-light)" stroke="var(--rim-dark)" stroke-width="4"/>

    <ellipse class="lens-outer" cx="705" cy="425" rx="342" ry="218"
      fill="url(#body-fill)" stroke="var(--rim-dark)" stroke-width="7"/>
    <ellipse class="lens-shadow" cx="698" cy="432" rx="318" ry="196"
      fill="var(--ink)" stroke="var(--rim-light)" stroke-width="3"/>
    <ellipse class="lens-ring" cx="728" cy="458" rx="280" ry="190"
      fill="url(#body-fill)" stroke="var(--rim-dark)" stroke-width="5"/>
    <ellipse class="lens-glass" cx="728" cy="456" rx="252" ry="170"
      fill="var(--ink)" stroke="var(--rim-light)" stroke-width="3"/>
  </svg>

  <p class="holder-name">CORINNE</p>
  <p class="phone-label">PHONE</p>
  <p class="phone-number">757-418-2296</p>

  <div class="brand">
    <span class="brand-dot"></span>
    <p class="brand-name">RVM PHOTOGRAPHY</p>
  </div>
</main>
</body>
</html>
```